Target Market(s)

Young, male, tech savvy, cryptocurrency investors

Industry/Entity Type

Information Technology

Logo Text

Coding

Coded - Design and coding required

Number of Pages Required

1 page

Font styles to use
Sans Serif

Colors

Designer to choose colors to be used in the design.

Requirements
Must have

```html
<!DOCTYPE html>
<html lang="en">
<head>
<meta charset="utf-8">
<title>Kyron Network</title>
<link href="https://fonts.googleapis.com/css2?family=Lato:wght@300;400;700;900&display=swap" rel="stylesheet">
<style>
:root{
  --hero-dark:#2e1a08;
  --hero-mid:#6b3c0c;
  --hero-glow:#e8941c;
  --orange:#c9762a;
  --orange-light:#e0963f;
  --orange-edge:#f08a30;
  --band:#d99a3c;
  --footer:#3b2410;
  --white:#ffffff;
  --cream:#f6e6d2;
  --black:#141414;
}
*{margin:0;padding:0;box-sizing:border-box}
html,body{width:1007px;height:1200px;overflow:hidden}
body{font-family:'Lato',sans-serif;background:var(--footer);color:var(--white);position:relative}
.hero{position:absolute;left:0;top:0;width:1007px;height:540px;
  background:radial-gradient(circle at 563px 230px,#ffcc55 0,var(--hero-glow) 90px,#a85e12 170px,var(--hero-mid) 260px,var(--hero-dark) 480px)}
.brand{position:absolute;left:80px;top:48px;display:flex;align-items:center;gap:10px}
.brand-mark{width:58px;height:58px;border-radius:50%;border:4px solid #e6a52c}
.brand-name{font-weight:700;font-size:22px;color:var(--cream);letter-spacing:-0.3px}
.menu-btn{position:absolute;left:878px;top:54px;width:45px;height:45px;border:2px solid var(--white);border-radius:50%;display:flex;flex-direction:column;justify-content:center;align-items:center;gap:4px}
.menu-btn span{display:block;width:18px;height:3px;background:var(--white);border-radius:2px}
.caption{position:absolute;left:172px;top:183px;width:663px;height:128px;border:1px solid rgba(255,255,255,.6);background:rgba(30,18,6,.6);text-align:center}
.caption h1{font-weight:900;font-size:28px;margin-top:30px;letter-spacing:-0.3px;text-shadow:0 2px 3px rgba(0,0,0,.5)}
.caption p{font-size:27px;font-weight:400;margin-top:5px}
.dots{position:absolute;left:477px;top:374px;display:flex;gap:4px}
.dots span{width:10px;height:10px;border-radius:50%;border:1.5px solid var(--white)}
.dots span.on{background:var(--white)}
.timeline-bg{position:absolute;left:0;top:300px}
.section-title{position:absolute;left:0;width:1007px;top:476px;text-align:center;font-weight:400;font-size:30px;letter-spacing:.5px}
.divider{position:absolute;left:452px;top:516px}
.card{position:absolute;top:559px;width:266px;height:257px;box-shadow:0 1px 4px rgba(0,0,0,.15)}
.card-art{position:absolute;left:0;top:0}
.card-date{position:absolute;top:186px;left:0;width:100%;text-align:center;font-weight:700;font-size:15px;display:flex;justify-content:center;align-items:center;gap:6px}
.card-date svg{display:block}
.card-text{position:absolute;top:213px;left:20px;right:20px;text-align:center;font-size:12px;line-height:17px;text-transform:uppercase}
.signup{position:absolute;left:0;top:878px;width:1007px;height:88px;background:linear-gradient(90deg,#d08a30,#e6ac52 50%,#d6953a)}
.signup h2{position:absolute;left:146px;top:33px;font-weight:900;font-size:19px}
.signup .email{position:absolute;left:278px;top:28px;width:468px;height:33px;background:var(--white);border:none;font-family:'Lato',sans-serif;font-size:10px;padding-left:24px;color:#444}
.signup .submit{position:absolute;left:751px;top:28px;width:110px;height:33px;background:linear-gradient(#2a2a2a,var(--black));color:var(--white);border:none;font-family:'Lato',sans-serif;font-weight:700;font-size:12px;letter-spacing:1px}
.footer{position:absolute;left:0;top:966px;width:1007px;height:234px;background:radial-gradient(ellipse at 500px 0,#4a2d12,var(--footer) 70%)}
.social{position:absolute;left:403px;top:40px;display:flex;gap:18px}
.social a{width:36px;height:36px;border:2px solid var(--cream);border-radius:50%;display:flex;align-items:center;justify-content:center}
.footer-rule{position:absolute;left:370px;top:103px;width:268px;height:2px;background:var(--cream)}
.footer-nav{position:absolute;top:135px;left:0;width:1007px;display:flex;justify-content:center;gap:18px;font-size:11px;color:var(--cream);text-transform:uppercase}
.footer-nav i{font-style:normal}
.copyright{position:absolute;top:176px;width:1007px;text-align:center;font-size:11px;color:var(--cream)}
</style>
</head>
<body>
<header class="hero" role="img" aria-label="Glowing golden coin surrounded by circuit board lines">
  <div class="brand"><span class="brand-mark"></span><span class="brand-name">KYRON NETWORK</span></div>
  <div class="menu-btn"><span></span><span></span><span></span></div>
  <div class="caption">
    <h1>THE WORLD’S MOST ADVANCED BLOCKCHAIN</h1>
    <p>The widest token distribution</p>
  </div>
  <div class="dots"><span class="on"></span><span></span><span></span><span></span></div>
</header>

<svg class="timeline-bg" width="1007" height="578" viewBox="0 300 1007 578">
  <defs>
    <radialGradient id="orangeFill" cx="0.5" cy="0.3" r="0.7">
      <stop offset="0" stop-color="#d58a38"/><stop offset="1" stop-color="#bf6e24"/>
    </radialGradient>
    <linearGradient id="cardBase" x1="0" y1="0" x2="0" y2="1"><stop offset="0" stop-color="#d58a3a"/><stop offset="1" stop-color="#e8a45a"/></linearGradient>
  </defs>
  <path d="M0 528 Q503.5 312 1007 528 L1007 878 L0 878 Z" fill="url(#orangeFill)"/>
  <path d="M0 528 Q503.5 312 1007 528" fill="none" stroke="#f5a650" stroke-width="4"/>
</svg>

<h2 class="section-title">TIMELINE</h2>
<svg class="divider" width="103" height="16" viewBox="0 0 103 16">
  <line x1="0" y1="8" x2="38" y2="8" stroke="#fff" stroke-width="1"/>
  <line x1="65" y1="8" x2="103" y2="8" stroke="#fff" stroke-width="1"/>
  <circle cx="51.5" cy="6" r="4" fill="none" stroke="#fff" stroke-width="1.5"/>
  <line x1="51.5" y1="10" x2="51.5" y2="15" stroke="#fff" stroke-width="2"/>
</svg>

<article class="card" style="left:82px">
  <svg class="card-art" width="266" height="257" viewBox="0 0 266 257">
    <rect width="266" height="200" fill="#7a4a12" role="img" aria-label="Golden coin emblem in front of a glowing grid"/>
    <path d="M0 199 Q133 103 266 199 L266 257 L0 257 Z" fill="url(#cardBase)"/>
    <path d="M0 199 Q133 103 266 199" fill="none" stroke="#fff" stroke-width="3"/>
  </svg>
  <div class="card-date"><svg width="13" height="13" viewBox="0 0 12 12"><rect x="0.5" y="2" width="11" height="9.5" fill="none" stroke="#fff"/><rect x="0.5" y="2" width="11" height="3" fill="#fff"/></svg>SEPT 2017</div>
  <p class="card-text">Etheris network airdrop</p>
</article>

<article class="card" style="left:370px">
  <svg class="card-art" width="266" height="257" viewBox="0 0 266 257">
    <rect width="266" height="200" fill="#2c3f7a" role="img" aria-label="Close-up of a gold coin lying on a stack of coins"/>
    <rect x="120" width="146" height="200" fill="#b88a2e" opacity=".5"/>
    <path d="M0 199 Q133 103 266 199 L266 257 L0 257 Z" fill="url(#cardBase)"/>
    <path d="M0 199 Q133 103 266 199" fill="none" stroke="#fff" stroke-width="3"/>
  </svg>
  <div class="card-date"><svg width="13" height="13" viewBox="0 0 12 12"><rect x="0.5" y="2" width="11" height="9.5" fill="none" stroke="#fff"/><rect x="0.5" y="2" width="11" height="3" fill="#fff"/></svg>OCT 2017</div>
  <p class="card-text">Bitcrest network linked address airdrop</p>
</article>

<article class="card" style="left:658px">
  <svg class="card-art" width="266" height="257" viewBox="0 0 266 257">
    <rect width="266" height="200" fill="#1e2a3c" role="img" aria-label="Hand touching a smartphone with a glowing coin on screen"/>
    <path d="M0 199 Q133 103 266 199 L266 257 L0 257 Z" fill="url(#cardBase)"/>
    <path d="M0 199 Q133 103 266 199" fill="none" stroke="#fff" stroke-width="3"/>
  </svg>
  <div class="card-date"><svg width="13" height="13" viewBox="0 0 12 12"><rect x="0.5" y="2" width="11" height="9.5" fill="none" stroke="#fff"/><rect x="0.5" y="2" width="11" height="3" fill="#fff"/></svg>NOV 2017</div>
  <p class="card-text">Proof-of-individuality human airdrop</p>
</article>

<section class="signup">
  <h2>SIGNUP NOW</h2>
  <input class="email" type="email" placeholder="Enter Email..">
  <button class="submit">SIGN UP</button>
</section>

<footer class="footer">
  <div class="social">
    <a aria-label="Share"><svg width="18" height="18" viewBox="0 0 18 18"><circle cx="4" cy="9" r="2.5" fill="#f6e6d2"/><circle cx="14" cy="4" r="2.5" fill="#f6e6d2"/><circle cx="14" cy="14" r="2.5" fill="#f6e6d2"/><path d="M4 9 L14 4 M4 9 L14 14" stroke="#f6e6d2" stroke-width="1.5"/></svg></a>
    <a aria-label="Chat"><svg width="18" height="18" viewBox="0 0 18 18"><path d="M2 3 H16 V12 H8 L4 15 V12 H2 Z" fill="#f6e6d2"/></svg></a>
    <a aria-label="News feed"><svg width="18" height="18" viewBox="0 0 18 18"><circle cx="4" cy="14" r="2" fill="#f6e6d2"/><path d="M2 8 A8 8 0 0 1 10 16" fill="none" stroke="#f6e6d2" stroke-width="2.2"/><path d="M2 3 A13 13 0 0 1 15 16" fill="none" stroke="#f6e6d2" stroke-width="2.2"/></svg></a>
    <a aria-label="Email"><svg width="18" height="18" viewBox="0 0 18 18"><rect x="2" y="4" width="14" height="10" fill="none" stroke="#f6e6d2" stroke-width="1.6"/><path d="M2 4 L9 10 L16 4" fill="none" stroke="#f6e6d2" stroke-width="1.6"/></svg></a>
  </div>
  <div class="footer-rule"></div>
  <nav class="footer-nav">
    <span>Home</span><i>•</i><span>About Us</span><i>•</i><span>Timeline</span><i>•</i><span>Cryptocurrency</span><i>•</i><span>Contact Us</span>
  </nav>
  <p class="copyright">© copyright 2017 Kyron.network . All rights reserved</p>
</footer>
</body>
</html>
```